New Website Design for High Quality Sailing School

This client has revised it's logo and branding and wants to create a new website that delivers a high-quality compelling design. Please read the brief, wireframes, brand guidelines and logos really carefully before you start your design work.
Note that the winning designer, based on the homepage, will be expected to do the other internal page designs as a part of this project.

Target Market(s)

Mainly Young Adults (20-35), High Net Worth, Love Sailing and Adventures

Industry/Entity Type

Leisure

Number of Pages Required

5+ page

Font styles to use
Sans Serif
Other font styles liked:
• Hyperspace Race

Requirements
Must have
• Attention to detail, high quality designs, applying the new branding carefully, and clean as per the brief.
Nice to have
• Keep it simple, but use the imagery. Take a look at the sites they like.
Should not have
• Inconsistency in design theme

```html
<!DOCTYPE html>
<html lang="en">
<head>
<meta charset="utf-8">
<title>Halyard Sailing</title>
<link rel="stylesheet" href="https://fonts.googleapis.com/css2?family=Oswald:wght@300;400;500&family=Montserrat:wght@400;500;600;700&display=swap">
<style>
  :root {
    --red: #f20000;
    --ink: #1c2430;
    --text: #2a3140;
    --white: #ffffff;
    --sea-top: #6d97c4;
    --sea-mid: #3d6fa8;
    --sea-deep: #1d3f6e;
    --panel: rgba(190, 215, 235, 0.45);
  }
  * { box-sizing: border-box; margin: 0; padding: 0; }
  html, body { width: 915px; height: 1200px; overflow: hidden; background: var(--white); }
  body { position: relative; font-family: "Montserrat", sans-serif; color: var(--text); }

  .top-rule { position: absolute; left: 0; top: 0; width: 915px; height: 4px; background: var(--red); }
  .utility-tab { position: absolute; left: 571px; top: 0; width: 344px; height: 26px; }
  .utility-nav { position: absolute; top: 6px; left: 596px; display: flex; gap: 11px;
    font-family: "Oswald", sans-serif; font-weight: 300; font-size: 8.5px; color: var(--white); text-transform: uppercase; }

  .brand { position: absolute; left: 116px; top: 34px; display: flex; align-items: center; gap: 8px; }
  .brand-mark { width: 14px; height: 14px; border-radius: 50%; background: var(--red); }
  .brand-name { font-family: "Montserrat", sans-serif; font-weight: 500; font-size: 13px;
    letter-spacing: 2px; color: #3a3f48; text-transform: uppercase; }

  .main-nav { position: absolute; top: 51px; left: 455px; display: flex; gap: 19px;
    font-family: "Oswald", sans-serif; font-weight: 400; font-size: 11.5px; color: var(--ink); text-transform: uppercase; }

  .hero { position: absolute; left: 0; top: 81px; width: 915px; height: 396px; overflow: hidden;
    background: linear-gradient(180deg, var(--sea-top) 0%, var(--sea-mid) 55%, var(--sea-deep) 100%); }
  .hero-photo { position: absolute; inset: 0;
    background: radial-gradient(ellipse 220px 260px at 720px 230px, rgba(240,244,248,0.75), rgba(240,244,248,0) 70%); }
  .hero-panel { position: absolute; left: 0; top: 0; width: 378px; height: 396px;
    background: var(--panel); border-radius: 0 27px 27px 0; }
  .hero-title { position: absolute; left: 126px; top: 170px; font-family: "Oswald", sans-serif;
    font-weight: 500; font-size: 32px; line-height: 38px; color: var(--ink); text-transform: uppercase; }
  .hero-sub { position: absolute; left: 126px; top: 294px; font-family: "Oswald", sans-serif;
    font-weight: 300; font-size: 23px; color: var(--ink); text-transform: uppercase; }
  .hero-cta { position: absolute; left: 126px; top: 264px; width: 191px; height: 41px; background: var(--red);
    color: var(--white); font-family: "Montserrat", sans-serif; font-weight: 500; font-size: 15px; letter-spacing: 0.5px;
    display: flex; align-items: center; justify-content: center; }
  .hero-dots { position: absolute; left: 414px; top: 365px; display: flex; gap: 5px; }
  .hero-dots span { width: 14px; height: 5px; border-radius: 3px; background: var(--white); }
  .hero-dots .active { background: #e8391d; }

  .destination { position: absolute; }
  .destination-photo { position: absolute; width: 286px; height: 286px; }
  .photo-croatia { left: 133px; top: 504px; background: linear-gradient(180deg, #b4bde0 0%, #4a5f8c 45%, #2b4370 100%); }
  .photo-mallorca { left: 500px; top: 854px; background: linear-gradient(160deg, #0d6d86 0%, #1b98ad 45%, #7a5a4a 70%, #2a8fa0 100%); }
  .destination-title { font-family: "Montserrat", sans-serif; font-weight: 700; font-size: 18.5px; color: var(--red); text-transform: uppercase; }
  .destination-lead { margin-top: 10px; font-size: 9.8px; line-height: 14.5px; text-transform: uppercase; color: var(--ink); letter-spacing: 0.2px; }
  .destination-list { list-style: none; margin-top: 19px; font-size: 9.4px; line-height: 14.3px; color: var(--ink); }
  .destination-list li { position: relative; padding-left: 18px; }
  .destination-list li::before { content: ""; position: absolute; left: 4px; top: 4px; width: 5px; height: 5px; border: 1.2px solid var(--red); }
  .enquire { margin-top: 30px; width: 115px; height: 28px; background: var(--red); color: var(--white);
    font-weight: 600; font-size: 8.5px; display: flex; align-items: center; justify-content: center; text-transform: uppercase; }
  .croatia { left: 475px; top: 543px; }
  .mallorca { left: 137px; top: 891px; }
</style>
</head>
<body>
  <div class="top-rule"></div>
  <svg class="utility-tab" viewBox="0 0 344 26" aria-hidden="true"><polygon points="0,0 344,0 344,26 12,26" fill="#f20000"/></svg>
  <nav class="utility-nav"><span>Blog</span><span>Gallery</span><span>About us</span><span>Instructors</span><span>Contact us</span></nav>

  <div class="brand"><span class="brand-mark"></span><span class="brand-name">Halyard Sailing</span></div>
  <nav class="main-nav"><span>Destinations</span><span>Liveaboard courses</span><span>Our tribe</span><span>Online masterclasses</span></nav>

  <section class="hero">
    <div class="hero-photo" role="img" aria-label="Sailing yacht with white sails on open blue sea, small rocky island on the left"></div>
    <div class="hero-panel"></div>
    <h1 class="hero-title" style="top:90px">Live the life of<br>adventure you've<br>dreamed of...</h1>
    <p class="hero-sub" style="top:213px">Learn to sail in a week</p>
    <a class="hero-cta">EMAIL NOW</a>
    <div class="hero-dots"><span></span><span class="active"></span><span></span><span></span><span></span></div>
  </section>

  <div class="destination-photo photo-croatia" role="img" aria-label="Sailor racing a small dinghy through choppy water"></div>
  <div class="destination croatia">
    <h2 class="destination-title">Trogir, Croatia</h2>
    <p class="destination-lead">Croatia is truly one of the most incredible<br>destinations in Europe to explore on a sailboat!</p>
    <ul class="destination-list">
      <li>Lorem ipsum dolor sit amet, consectetur</li>
      <li>Sed do eiusmod tempor incididunt ut labore et. Dolore</li>
      <li>magna aliqua. Quis ipsum suspendisse. Risus commodo</li>
      <li>viverra maecenas accumsan lacus Sed do eiusmod.</li>
      <li>Di di dii di indwsiajstempor</li>
    </ul>
    <a class="enquire">Enquire now</a>
  </div>

  <div class="destination mallorca">
    <h2 class="destination-title">Mallorca, Spain.</h2>
    <p class="destination-lead">Visit ancient towns and spectacular beaches while<br>enjoying the vibrant Spanish culture and food</p>
    <ul class="destination-list">
      <li>Lorem ipsum dolor sit amet, consectetur</li>
      <li>Sed do eiusmod tempor incididunt ut labore et. Dolore</li>
      <li>magna aliqua. Quis ipsum suspendisse. Risus commodo</li>
      <li>viverra maecenas accumsan lacus Sed do eiusmod.</li>
      <li>Di di dii di indwsiajstempor</li>
    </ul>
    <a class="enquire">Enquire now</a>
  </div>
  <div class="destination-photo photo-mallorca" role="img" aria-label="Rocky pine-covered coastline above turquoise sea"></div>
</body>
</html>
```